illustration of the importance of using your money as voting power for the environment

Illustration to read either per word, or creative interpretation (open to suggestions) " Vote, use your $ to vote for your favourite candidate" and then below it will have two choices the first reading "Berries- imported (yes), regulated (questionable), Free trade over Free Health (absolutely)" second choice reading "Berries- local (yes), organic (hopefully), regulated (most definatley) Free trade over Free Health (not on Australia's watch). there will be a little thought bubble next to the second choice that says "I know we cost more, but do you think people will get it yet?). It must have my logo on the bottom. I have uploaded the file.

The project is about using your money or your wallet to make a choice, making that choice is equal to voting. Every time you buy something, you are voting for a 'good' project, one that is environmentally friendly and gives positvely to the environment OR you are voting/buying a 'bad' product that is unsustainable, potentially poisonous and damages people and the environment. We just had a health scare here becuase of imported berries that were not regulated because of our new free trade agreement with china, although this is not about china, its about be aware as a consumer and making or Voting for your future.

Target Market(s)

20's- 50's

Industry/Entity Type

Environment

Requirements
Must have
• my logo and business name

```html
<!DOCTYPE html>
<html lang="en">
<head>
<meta charset="utf-8">
<title>Vote With Your Dollar</title>
<link rel="stylesheet" href="https://fonts.googleapis.com/css2?family=Oswald:wght@500&family=Open+Sans:wght@300;400&family=Arimo:wght@400;700&family=Yanone+Kaffeesatz:wght@300&family=Cinzel:wght@700&display=swap">
<style>
  :root {
    --wood-light: #9c7d5e;
    --wood-mid: #7a5c40;
    --wood-dark: #4a3423;
    --ink: #2e261f;
    --ink-soft: rgba(40, 31, 24, 0.78);
    --chalk: #ffffff;
    --band: rgba(230, 220, 205, 0.35);
    --bubble: #3dbdb5;
    --bubble-text: #e8f3f1;
    --berry-blue: #3f5470;
    --berry-red: #b51d2a;
    --brand-green: #6fa82a;
    --brand-ink: #1d1d1b;
  }
  * { margin: 0; padding: 0; box-sizing: border-box; }
  html, body { width: 1200px; height: 898px; overflow: hidden; background: var(--wood-mid); }
  .poster { position: relative; width: 1200px; height: 898px; overflow: hidden; }
  .wood-backdrop {
    position: absolute; inset: 0;
    background:
      linear-gradient(180deg, rgba(255,255,255,0) 0 60%, rgba(40,25,15,0.35) 100%),
      linear-gradient(90deg, var(--wood-mid) 0%, var(--wood-light) 30%, #a88a6c 55%, var(--wood-light) 75%, var(--wood-dark) 100%);
  }
  .berries {
    position: absolute; right: 0; top: 0; width: 385px; height: 330px;
    background: radial-gradient(circle at 70% 20%, var(--berry-red) 0 18%, transparent 30%),
                radial-gradient(circle at 40% 55%, var(--berry-blue) 0 30%, transparent 55%),
                radial-gradient(circle at 90% 70%, var(--berry-blue) 0 20%, transparent 40%);
    border-bottom-left-radius: 60% 70%;
  }
  .headline {
    position: absolute; left: 222px; top: 8px;
    font-family: 'Arimo', sans-serif; font-weight: 400;
    font-size: 260px; line-height: 1; letter-spacing: -18px;
    color: var(--ink-soft); white-space: nowrap;
    -webkit-text-stroke: 2px rgba(240,230,215,0.45);
  }
  .call-band {
    position: absolute; left: 35px; top: 258px; width: 1107px; height: 100px;
    background: var(--band); border-radius: 8px;
    display: flex; align-items: center; padding-left: 40px;
  }
  .call-text {
    display: flex; align-items: center;
    font-family: 'Cinzel', serif; font-weight: 700; font-size: 30px; line-height: 1;
    color: var(--ink-soft); font-variant: small-caps; white-space: nowrap;
  }
  .call-text .dollar {
    font-family: 'Oswald', sans-serif; font-weight: 500; font-size: 116px; line-height: 1;
    margin: 0 14px 0 26px; color: var(--ink);
  }
  .choice {
    position: absolute; font-family: 'Arimo', sans-serif; font-weight: 700;
    font-size: 36px; color: var(--chalk); line-height: 1.05;
    border-bottom: 3px double var(--chalk); padding-bottom: 2px;
    text-shadow: 0 1px 2px rgba(0,0,0,0.4); white-space: nowrap;
  }
  .choice--stack { border-bottom: none; line-height: 1.2; }
  .choice--stack span { display: block; border-bottom: 3px double var(--chalk); width: fit-content; }
  .mark { position: absolute; filter: drop-shadow(0 3px 4px rgba(0,0,0,0.45)); }
  .mark path { fill: rgba(45,35,27,0.72); stroke: rgba(245,238,228,0.85); stroke-width: 3; stroke-linejoin: round; }
  .speech { position: absolute; left: 565px; top: 645px; width: 465px; height: 160px; }
  .speech-text {
    position: absolute; left: 585px; top: 650px; width: 400px;
    font-family: 'Yanone Kaffeesatz', sans-serif; font-weight: 300;
    font-size: 38px; line-height: 52px; color: var(--bubble-text);
  }
  .slogan { position: absolute; font-family: 'Open Sans', sans-serif; font-weight: 300; color: var(--chalk); line-height: 1; white-space: nowrap; }
  .slogan--free { left: 55px; top: 728px; font-size: 98px; }
  .slogan--trade { left: 257px; top: 763px; font-size: 30px; transform: rotate(90deg); transform-origin: center; letter-spacing: 2px; }
  .slogan--over { left: 345px; top: 716px; font-size: 58px; }
  .slogan--health { left: 398px; top: 784px; font-size: 74px; }
  .brand { position: absolute; left: 1040px; top: 812px; display: flex; align-items: center; gap: 6px; }
  .brand-dot { width: 26px; height: 26px; border-radius: 50%; background: var(--brand-green); }
  .brand-name { font-family: 'Open Sans', sans-serif; font-weight: 400; font-size: 22px; color: var(--brand-ink); }
</style>
</head>
<body>
<main class="poster">
  <div class="wood-backdrop" role="img" aria-label="Weathered wooden plank surface"></div>
  <div class="berries" role="img" aria-label="Fresh blackberries, raspberries and blueberries"></div>

  <h1 class="headline">!VOTE!</h1>

  <div class="call-band">
    <p class="call-text">Vote, use your<span class="dollar">$</span>to vote for our favorite candidate.</p>
  </div>

  <p class="choice" style="left:100px;top:400px">Berries Imported</p>
  <p class="choice" style="left:100px;top:478px">Berries Regulated</p>
  <p class="choice choice--stack" style="left:100px;top:553px"><span>Free trede over</span><span style="margin-left:30px">free health ??</span></p>

  <p class="choice" style="left:650px;top:398px">Berries local</p>
  <p class="choice" style="left:650px;top:478px">Organic</p>
  <p class="choice" style="left:650px;top:565px">Regulated</p>

  <svg class="mark" style="left:415px;top:365px" width="135" height="95" viewBox="0 0 135 95"><path d="M4 50 L22 36 L48 64 L118 4 L130 18 L48 90 Z"/></svg>
  <svg class="mark" style="left:425px;top:465px" width="80" height="72" viewBox="0 0 80 72"><path d="M6 6 H24 L40 26 L56 6 H74 L50 36 L74 66 H56 L40 46 L24 66 H6 L30 36 Z"/></svg>
  <svg class="mark" style="left:425px;top:550px" width="80" height="72" viewBox="0 0 80 72"><path d="M6 6 H24 L40 26 L56 6 H74 L50 36 L74 66 H56 L40 46 L24 66 H6 L30 36 Z"/></svg>

  <svg class="mark" style="left:900px;top:360px" width="135" height="95" viewBox="0 0 135 95"><path d="M4 50 L22 36 L48 64 L118 4 L130 18 L48 90 Z"/></svg>
  <svg class="mark" style="left:900px;top:450px" width="135" height="95" viewBox="0 0 135 95"><path d="M4 50 L22 36 L48 64 L118 4 L130 18 L48 90 Z"/></svg>
  <svg class="mark" style="left:900px;top:530px" width="135" height="95" viewBox="0 0 135 95"><path d="M4 50 L22 36 L48 64 L118 4 L130 18 L48 90 Z"/></svg>

  <svg class="speech" viewBox="0 0 465 160" aria-hidden="true">
    <path d="M16 0 H449 Q465 0 465 16 V94 Q465 110 449 110 H420 L366 156 L380 110 H16 Q0 110 0 94 V16 Q0 0 16 0 Z" fill="var(--bubble)"/>
  </svg>
  <p class="speech-text">I Know we cost more but do you think people will get it yet ?</p>

  <p class="slogan slogan--free">FREE</p>
  <p class="slogan slogan--trade">TRADE</p>
  <p class="slogan slogan--over">OVER</p>
  <p class="slogan slogan--health">FREE-HEALTH</p>

  <div class="brand">
    <span class="brand-dot"></span>
    <span class="brand-name">buyWise</span>
  </div>
</main>
</body>
</html>
```